meridale partners business card

Architectural firm business card
Updates

Please note:

corporate colour black+yellow are the only elements to be kept.
NO OTHER ELEMENT TO BE REUSED FROM PREVIOUS BUSINESS CARD.
Thank you.

Dear Everyone,

Thank you for your participation. I have upload the KBSO+ logo again for incoporate in the card. in tif and pdf format.

Thank you 

I keep getting request for the logo file. Does everyone has the same problem?

I cannot do much, because the file is upload to the website server. I can't seem to see it either.

The logo file is now working. Please download. I check it myself. Thank you everyone.

Dear All,

Thank you for all the hard work. There are a lot of great work. Due to current commitment with work, I am unable to review them just yet. I will do so next week and advise everyone also. Thank you again. Best regards

Dear All,

Thank you for your participation. There are a lot of good design. Unfortunately, I can only select one. All the best. This is definitely a good crowd to work with. Thank you everyone again.

Best regards

Target Market(s)

Corporate, commercial and institutional projects only

Industry/Entity Type

Business

Requirements
Must have
• elegant simple
double sided with coating
Member of Southland Guild of Draughtsmen (logo only)
corporate colour black and

LOGO FILE UPLOADED
Should not have
• should not be the same as current business card.
upload for reference information only.
font sans serif preferred.

```html
<!DOCTYPE html>
<html lang="en">
<head>
<meta charset="utf-8">
<title>Meridale Partners – Business Card</title>
<link rel="stylesheet" href="https://fonts.googleapis.com/css2?family=Exo+2:wght@400&family=Open+Sans:wght@400&display=swap">
<style>
  :root {
    --backdrop: #e6e6e4;
    --brand-yellow: #f6bd4b;
    --brand-black: #0b0b0b;
    --ink-white: #ffffff;
    --card-shadow: rgba(0, 0, 0, 0.22);
  }
  * { box-sizing: border-box; margin: 0; padding: 0; }
  html, body {
    width: 1200px;
    height: 969px;
    overflow: hidden;
    background: var(--backdrop);
  }
  .sheet {
    position: relative;
    width: 1200px;
    height: 969px;
  }
  .card {
    position: absolute;
    left: 290px;
    width: 620px;
    height: 354px;
    overflow: hidden;
    box-shadow: 0 10px 28px var(--card-shadow);
  }

  /* Front side */
  .card--front {
    top: 100px;
    background: var(--brand-yellow);
    font-family: "Exo 2", sans-serif;
  }
  .card--front .band {
    position: absolute;
    left: 0; right: 0;
    top: 118px;
    height: 11px;
    background: var(--brand-black);
  }
  .services {
    position: absolute;
    right: 30px;
    top: 42px;
    text-align: right;
    color: var(--brand-black);
    font-weight: 400;
    font-size: 23px;
    line-height: 19px;
    letter-spacing: 0.5px;
  }
  .firm-name {
    position: absolute;
    left: 28px;
    top: 146px;
    color: var(--ink-white);
    font-weight: 400;
    font-size: 28px;
    line-height: 34px;
    letter-spacing: 0.5px;
    white-space: nowrap;
  }

  /* Back side */
  .card--back {
    top: 515px;
    background: var(--brand-black);
    color: var(--ink-white);
    font-family: "Open Sans", sans-serif;
  }
  .card--back .band {
    position: absolute;
    left: 0; right: 0;
    top: 152px;
    height: 17px;
    background: var(--brand-yellow);
  }
  .person {
    position: absolute;
    left: 40px;
    top: 22px;
  }
  .person__name {
    font-weight: 400;
    font-size: 30px;
    line-height: 38px;
    letter-spacing: 0.5px;
  }
  .person__role {
    font-size: 11px;
    line-height: 19px;
    margin-left: 8px;
    margin-top: 4px;
  }
  .office {
    position: absolute;
    left: 40px;
    top: 186px;
    font-size: 12.5px;
    line-height: 22px;
  }
  .office__name {
    font-size: 15px;
    margin-left: 16px;
    margin-bottom: 2px;
  }
  .office__line {
    display: flex;
    align-items: center;
    gap: 8px;
  }
  .office__line svg { width: 13px; height: 13px; flex: none; }
</style>
</head>
<body>
<main class="sheet">

  <section class="card card--front" aria-label="Card front">
    <div class="band"></div>
    <p class="services">architects<br>urban designers<br>project managers</p>
    <p class="firm-name">meridale partners</p>
  </section>

  <section class="card card--back" aria-label="Card back">
    <div class="person">
      <p class="person__name">Linh Carver</p>
      <p class="person__role">Architect<br>Director<br>0400 17 42 66</p>
    </div>
    <div class="band"></div>
    <div class="office">
      <p class="office__name">Harwick House</p>
      <p class="office__line">12 Ellery Street, Northvale NSW 2199</p>
      <p class="office__line">
        <svg viewBox="0 0 16 16" aria-hidden="true"><path fill="#fff" d="M4 1l2.5 3.5-1.6 1.6c.9 2 2.5 3.6 4.5 4.5l1.6-1.6L14.5 11.5 13 14c-6 0-11-5-11-11z"/></svg>
        +612 9000 4172 &nbsp;+612 9000 4173
      </p>
      <p class="office__line">
        <svg viewBox="0 0 16 16" aria-hidden="true"><rect x="1" y="3" width="14" height="10" fill="#fff"/><path d="M1 3l7 6 7-6" fill="none" stroke="#0b0b0b" stroke-width="1.3"/></svg>
        mail@meridalepartners.com.au
      </p>
      <p class="office__line">
        <svg viewBox="0 0 16 16" aria-hidden="true"><g fill="none" stroke="#fff" stroke-width="1.2"><circle cx="8" cy="8" r="6.5"/><ellipse cx="8" cy="8" rx="3" ry="6.5"/><path d="M1.5 8h13M2.5 4.8h11M2.5 11.2h11"/></g></svg>
        www.meridalepartners.com.au
      </p>
    </div>
  </section>

</main>
</body>
</html>
```